Crossroads of Marriage Website Design

The primary objectives of this website is lead generation, create authority and enhance trust factor so that potential clients utilize Crossroads of Marriage services.

In an effort to provide prospects with a comprehensive explanation of the company’s services, Crossroads of Marriage will be creating a new website to provide, a user-friendly experience that will lead a person onto the right pathway where they will find tailored information depending on the stage they are in: Thinking of Divorce, Ready to Move Forward, and Recently Divorced.

Visitors will land on the homepage, which will give them the opportunity to select from the three types of personas shown. Messaging will be written specifically for each persona type, a lead-gen form will be present throughout the entire site, and a free downloadable form will be provided to them.

Once the lead gen form is submitted, information will be sent to Crossroads of Marriage consultant, who will follow up with the prospect.

Social Integration with website continue to prove Crossroads of Marriage authority and expertise.

Target Market(s)

Individuals who are considering or our in the process of divorce find themselves in a state of trying to make sense of it all. They lack the knowledge they need concerning the divorce process. Both men and women are typically scared of the unknown and financial loss. Due to the emotional stress they hire an attorney quickly that may not be suitable to their personality and/or situation.

Both men and women need an unbiased and informed partner that can guide them in the right direction. Time is their most precious commodity; making costly mistakes might ruin their financial situation, enhance their stress levels and prolong the divorce process. Both parties are looking for the right answers, the right professional divorce team, i.e. lawyer, mediator, financial planner, etc. to help them get their lives back in order.

Demographics
• Men and Women
• Ages 36 to 55
• Income: 80K+ per person or $150K+ combined
• Working Professionals: dentist, managers, creative directors, bankers, etc.

Industry/Entity Type

It Company

Requirements
Must have
• Visual Feeling
• The look and feel should represent a feeling of trust and reliability.
• Use colors from the logo.
• Please select images from Q-Frame Images
• Please refer to wireframes to see where images should be placed
• Calls To Action should stand out on each page.

Use the new logo Crossroads of Marriage Logo and tagline: Answers, Referrals, Support.

Please use the following URL: www.crossroadsofimarriage.com

```html
<!DOCTYPE html>
<html lang="en">
<head>
<meta charset="utf-8">
<title>Crossroads of Marriage</title>
<link rel="stylesheet" href="https://fonts.googleapis.com/css2?family=Ubuntu:wght@400;500&family=Lato:wght@400;700&display=swap">
<style>
:root{
  --green:#4e8a2c;
  --green-dark:#3f7322;
  --blue:#3f78c8;
  --blue-light:#5a93db;
  --blue-dark:#2d5fa8;
  --hero:#6e6968;
  --ink:#3a3a3a;
  --muted:#555;
  --rule:#d9d9d9;
  --white:#fff;
}
*{margin:0;padding:0;box-sizing:border-box}
html,body{width:1067px;height:1200px;overflow:hidden;background:var(--white)}
body{position:relative;font-family:"Lato",sans-serif;color:var(--ink)}
.abs{position:absolute}

/* header */
.brand{left:107px;top:22px;width:200px;height:90px;display:flex;align-items:flex-end;gap:8px}
.brand-mark{width:18px;height:18px;background:var(--green);flex:none;margin-bottom:6px}
.brand-name{font-family:"Ubuntu",sans-serif;font-weight:500;font-size:19px;line-height:1.1;color:var(--green)}
.call{left:752px;top:24px;width:206px;height:54px;border:1px solid #e2e2e2;border-radius:27px;display:flex;align-items:center;padding-left:22px;gap:16px}
.call-text{font-family:"Ubuntu",sans-serif;font-size:20px;line-height:22px;color:var(--green)}
.share{left:628px;top:97px;height:19px;display:flex;gap:3px;font-size:9.5px;background:#f1f1f1;padding:1px 3px}
.share span{border:1px solid #ccc;background:#fff;padding:2px 4px;line-height:11px}
.share .count{border-color:transparent;background:#f1f1f1}
.share i{display:inline-block;width:9px;height:9px;background:var(--blue);margin-right:3px;vertical-align:-1px}

/* nav */
.hero{left:0;top:150px;width:1067px;height:431px;background:linear-gradient(90deg,#625d5c,#7a7473 50%,#666160)}
.nav{left:107px;top:128px;width:853px;height:40px;display:flex;background:linear-gradient(var(--blue-light),var(--blue));box-shadow:0 1px 2px rgba(0,0,0,.3)}
.nav a{font-family:"Ubuntu",sans-serif;font-size:16px;color:var(--white);text-decoration:none;display:flex;align-items:center;justify-content:center}
.nav a.active{background:linear-gradient(#5c9b35,var(--green))}

/* persona cards */
.card{width:276px;height:142px}
.card-photo{position:absolute;inset:0}
.card-label{position:absolute;left:0;top:45px;height:40px;background:rgba(40,40,40,.75);color:#fff;font-family:"Ubuntu",sans-serif;font-size:12.5px;display:flex;align-items:center;padding:0 12px}
.btn{position:absolute;left:18px;top:105px;width:83px;height:32px;background:linear-gradient(var(--blue-light),var(--blue-dark));color:#fff;font-family:"Ubuntu",sans-serif;font-size:12.5px;display:flex;align-items:center;justify-content:center;box-shadow:0 1px 2px rgba(0,0,0,.35)}
.promo{left:614px;top:274px;width:346px;height:206px;background:var(--green);color:#fff;text-align:center;font-family:"Ubuntu",sans-serif}
.promo h2{font-weight:400;font-size:17px;margin-top:52px}
.promo p{font-size:11.5px;margin-top:6px}
.promo .cta{position:absolute;left:23px;top:112px;width:302px;height:46px;background:linear-gradient(var(--blue-light),var(--blue-dark));display:flex;align-items:center;justify-content:center;font-size:16px;box-shadow:0 1px 3px rgba(0,0,0,.35)}

/* copy */
.copy{left:105px;top:602px;width:857px;font-size:10.6px;line-height:16px;color:var(--muted);text-align:justify;hyphens:auto;-webkit-hyphens:auto}
.copy p+p{margin-top:16px}
.rule{left:107px;width:853px;height:1px;background:var(--rule)}
.seen{left:107px;top:806px;font-size:10.5px}
.badge{top:842px;height:80px;border:1px solid #d5d5d5;display:flex;align-items:center;justify-content:center}
.badge div{width:72%;height:30px;background:#c9c9c9}

/* footer */
.foot-h{top:968px;font-family:"Lato",sans-serif;font-weight:700;font-size:12px;color:#333}
.links{left:106px;top:995px;list-style:none;font-size:10.5px;line-height:17.8px;color:#444}
.testi{left:257px;top:998px;width:195px;height:170px;border:1px solid #d5d5d5;padding:10px 7px}
.testi h3{font-family:"Ubuntu",sans-serif;font-weight:400;font-size:13.5px}
.testi p{font-size:9.5px;line-height:14.3px;margin-top:10px;text-align:justify;color:#444}
.next{position:absolute;right:8px;bottom:8px;width:53px;height:22px;background:linear-gradient(var(--blue-light),var(--blue-dark));color:#fff;font-size:9px;font-weight:700;display:flex;align-items:center;justify-content:center}
.contact{left:486px;top:1010px;font-size:10.5px;color:#444;width:185px}
.contact strong{display:block;font-size:12px;color:#333}
.field{left:685px;width:266px;height:30px;border:1px solid #ccc;font-size:10.5px;padding:9px 7px;color:#444}
.submit{left:877px;top:1077px;width:73px;height:30px;background:linear-gradient(var(--blue-light),var(--blue-dark));color:#fff;font-family:"Ubuntu",sans-serif;font-size:12.5px;display:flex;align-items:center;justify-content:center}
.follow{left:685px;top:1117px;width:266px;height:39px;border:1px solid #ccc;display:flex;align-items:center;justify-content:center;gap:8px;font-family:"Ubuntu",sans-serif;font-size:15.5px;color:#333}
.follow span.sq{width:25px;height:25px;background:var(--blue-dark);display:inline-block}
.follow span.sq:first-of-type{margin-left:16px}
</style>
</head>
<body>

<header>
  <div class="abs brand"><span class="brand-mark"></span><span class="brand-name">Crossroads of Marriage</span></div>
  <div class="abs call">
    <svg width="20" height="26" viewBox="0 0 20 26" aria-hidden="true"><path d="M5 2c2 0 3 4 3 6s-3 2-3 3 2 6 5 7c1 0 2-3 3-3s4 2 4 4-2 3-4 3C7 22 1 12 1 6 1 4 3 2 5 2z" fill="#3d3d3d"/></svg>
    <div class="call-text">CALL US ON<br>555.014.2290</div>
  </div>
  <div class="abs share">
    <span><i></i>Share</span><span class="count">253K</span>
    <span><i></i>Friendly</span><span class="count">245K</span>
    <span><i></i>Chirper</span><span class="count">7K</span>
    <span><i style="background:#888"></i>Email</span>
  </div>
</header>

<div class="abs hero" role="img" aria-label="Faded photo of a couple talking at home"></div>

<nav class="abs nav">
  <a class="active" href="#" style="width:145px">ABOUT US</a>
  <a href="#" style="width:170px">SERVICES</a>
  <a href="#" style="width:165px">RESOURCES</a>
  <a href="#" style="width:205px">TAKE CONTROL</a>
  <a href="#" style="width:168px">CONTACT US</a>
</nav>

<section>
  <div class="abs card" style="left:107px;top:187px">
    <div class="card-photo" role="img" aria-label="Photo of a thoughtful woman" style="background:linear-gradient(90deg,#e7e2de,#c9a898 60%,#7a5a4d)"></div>
    <div class="card-label">THINKING OF DIVORCE</div><div class="btn">READ MORE</div>
  </div>
  <div class="abs card" style="left:355px;top:240px">
    <div class="card-photo" role="img" aria-label="Photo of a couple seated apart at a table" style="background:linear-gradient(90deg,#d8d4cc,#b5aa95 50%,#8a8d5a)"></div>
    <div class="card-label">NEED TO DO SOMETHING</div><div class="btn">READ MORE</div>
  </div>
  <div class="abs card" style="left:107px;top:365px">
    <div class="card-photo" role="img" aria-label="Photo of a woman resting her head on a book" style="background:linear-gradient(90deg,#b08a78,#e5d8cc 60%,#f3efe9)"></div>
    <div class="card-label">RECENTLY DIVORCED</div><div class="btn">READ MORE</div>
  </div>
  <div class="abs card" style="left:355px;top:419px">
    <div class="card-photo" role="img" aria-label="Photo of a worried man over banknotes" style="background:linear-gradient(90deg,#8a8470,#b89d86 55%,#c7a18c)"></div>
    <div class="card-label">FINANCIAL HELP</div><div class="btn">READ MORE</div>
  </div>
  <div class="abs promo">
    <h2>TAKE THE "MYSTERY" OUT OF DIVORCE.</h2>
    <p>FIND OUT WHAT YOU NEED TO KNOW</p>
    <div class="cta">SCHEDULE YOUR FREE CONSULTATION.</div>
  </div>
</section>

<main class="abs copy">
  <p>Sed ut perspiciatis unde omnis iste natus error sit voluptatem accusantium doloremque laudantium, totam rem aperiam, eaque ipsa quae ab illo inventore veritatis et quasi architecto beatae vitae dicta sunt explicabo. Nemo enim ipsam voluptatem quia voluptas sit aspernatur aut odit aut fugit, sed quia consequuntur magni dolores eos qui ratione voluptatem sequi nesciunt. Neque porro quisquam est, qui dolorem ipsum quia dolor sit amet, consectetur, adipisci velit, sed quia non numquam eius modi tempora incidunt ut labore et dolore magnam aliquam quaerat voluptatem. Ut enim ad minima veniam, quis nostrum exercitationem ullam corporis suscipit laboriosam, nisi ut aliquid ex ea commodi consequatur? Quis autem vel eum iure reprehenderit qui in ea voluptate velit esse quam nihil molestiae consequatur, vel illum qui dolorem eum fugiat quo voluptas nulla pariatur</p>
  <p>Sed ut perspiciatis unde omnis iste natus error sit voluptatem accusantium doloremque laudantium, totam rem aperiam, eaque ipsa quae ab illo inventore veritatis et quasi architecto beatae vitae dicta sunt explicabo. Nemo enim ipsam voluptatem quia voluptas sit aspernatur aut odit aut fugit, sed quia consequuntur magni dolores eos qui ratione voluptatem sequi nesciunt. Neque porro quisquam est, qui dolorem ipsum quia dolor sit amet, consectetur, adipisci velit, sed quia non numquam eius modi tempora incidunt ut labore et dolore magnam aliquam quaerat voluptatem. Ut enim ad minima veniam, quis nostrum exercitationem ullam corporis suscipit laboriosam, nisi ut aliquid ex ea commodi consequatur? Quis autem vel eum iure reprehenderit qui in ea voluptate velit esse quam nihil molestiae consequatur, vel illum qui dolorem eum fugiat quo voluptas nulla pariatur</p>
</main>

<div class="abs rule" style="top:798px"></div>
<div class="abs seen">As Seen On:</div>
<div class="abs rule" style="top:827px"></div>
<div class="abs badge" style="left:107px;width:293px"><div></div></div>
<div class="abs badge" style="left:418px;width:257px"><div></div></div>
<div class="abs badge" style="left:702px;width:258px"><div></div></div>
<div class="abs rule" style="top:940px"></div>

<footer>
  <div class="abs foot-h" style="left:106px">Quick Links</div>
  <div class="abs foot-h" style="left:259px">What People are Saying</div>
  <div class="abs foot-h" style="left:490px">Get in Touch</div>
  <div class="abs foot-h" style="left:687px">Newsletter Educate Yourself</div>

  <ul class="abs links">
    <li>About Us</li><li>Services</li><li>Testimonials</li><li>Resources</li><li>Take Control</li><li>Contact Us</li><li>Privacy Policy</li><li>Terms</li><li>Disclaimers</li>
  </ul>

  <div class="abs testi">
    <h3>Testimonials</h3>
    <p>Sed ut perspiciatis unde omnis iste natus error sit voluptatem accusantium doloremque laudantium, totam rem aperiam, eaque ipsa quae ab illo inventore veritatis et quasi architecto beatae vitae dicta sunt explicabo. Nemo enim ipsam voluptatem quia</p>
    <div class="next">NEXT »</div>
  </div>

  <div class="abs contact">
    <div style="font-size:10px">© 2013 Crossroads of Marriage |</div>
    <strong style="margin-top:22px">Crossroads of Marriage</strong>
    <div style="line-height:14px">4120 Harbor Lane Ste 210 Bayview, Florida 33000</div>
    <strong style="margin-top:12px">555.014.2290</strong>
  </div>

  <div class="abs field" style="top:998px">First Name</div>
  <div class="abs field" style="top:1038px">Email</div>
  <div class="abs submit">SUBMIT</div>
  <div class="abs follow">Follow Us <span class="sq"></span><span class="sq"></span></div>
</footer>

</body>
</html>
```